Funk up our website

Our website is currently in operation and working well, see it at www.clearbriefhub.co.uk

However it needs some redesign work, to help it feel fresh, inviting and friendly.

We need graphic mockups (png hi-res) to pass to the dev team, to do the css work:

homepage - http://www.clearbriefhub.co.uk
topic page - http://www.clearbriefhub.co.uk/guidance/business
sub-topic - http://www.clearbriefhub.co.uk/guidance/business/goods-services
content - http://www.clearbriefhub.co.uk/guidance/business/goods-services/heads-of-terms
ancillary pages - contact us, heads of terms, etc

The structure of the page in terms of the placement of header, menu bar, content area and footer needs to remain, but the design of it is up for grabs.

The site is currently free to use, but in the future will have the aim of getting users to register for free, but with the option of buying documents on an individual basis, or subscription basis, or subscribing to additional legal services.

Additional information
---------------------------
Users
1. Owners and managers in small and medium businesses
2. In the UK only
3. Who find dealing with legal issues and lawyers intimidating
4. Who are searching for online help to try and avoid having to deal with a lawyer
5. Or have been referred via social media
Desired user experience
1. A welcoming, friendly site
2. That takes the complexity out of dealing with legal issues
3. That really does clear the brief
4. That is fast, efficient and clear
5. That is pleasantly different from the normal experience of interacting with a law firm
Relevant factors
1. Most visitors will first land on a content page (e.g. [link]) via a search result or banner advertisement – not the Home Page
2. Repeat visitors are more likely to go to the Home Page
3. Works with web responsive design techniques for display on smartphones and tablets
4. Implemented through CSS
Colour palette
Designer should feel able to build the palette around the following core colours
CMYK
YELLOW = 0,25,100,0
GREEN = 80,0,100,0
BLUE = 100,25,0,0

RGB
YELLOW = 255,195,15
GREEN = 15,175,75
BLUE = 0,140,210

PANTONE
YELLOW = 123c
GREEN = 361c
BLUE = 3005c

Fonts
Soho Gothic, Soho, Arial
Designer should feel able to add fonts to complement these core fonts.

Our logo needs to remain (see attached document) Our strap line, can be changed if needed.

Best
RK
Updates

Hi All

Some websites worth having a look at for how people have done things differently / added something distinctive to their website:

http://www.brevicounsel.co.uk/
https://www.tandelegal.co.uk/
http://www.quillatrix.com/

Cheers
RK

Hi All

Thanks for your designs. Just back in the office today, we will discuss and feedback / decide asap.

Best
RK

```html
<!DOCTYPE html>
<html lang="en">
<head>
<meta charset="utf-8">
<title>Clear Brief Hub — Home</title>
<link rel="stylesheet" href="https://fonts.googleapis.com/css2?family=Fira+Sans:wght@400;600;700&family=Arimo:wght@400;700&display=swap">
<style>
  :root {
    --yellow: #ffc30f;
    --green: #0faf4b;
    --blue: #008cd2;
    --header-blue: #2a8fd6;
    --charcoal: #383c44;
    --pill: #4b4f57;
    --red: #c8202f;
    --ink: #111111;
    --white: #ffffff;
    --icon-dark: #3a3a3a;
  }
  * { box-sizing: border-box; margin: 0; padding: 0; }
  html, body { width: 1081px; height: 1200px; overflow: hidden; background: var(--white); }
  body { position: relative; font-family: "Arimo", Arial, sans-serif; }

  .site-header { position: absolute; left: 0; top: 0; width: 1081px; height: 204px; background: var(--header-blue); }
  .brand-box { position: absolute; left: 0; top: 0; width: 203px; height: 204px; background: var(--white);
    display: flex; flex-direction: column; align-items: center; justify-content: center; gap: 12px; }
  .brand-mark { width: 58px; height: 58px; background: var(--green); }
  .brand-name { font-family: "Fira Sans", Arial, sans-serif; font-weight: 700; font-size: 15px; color: var(--ink); }

  .main-nav a { position: absolute; top: 86px; color: var(--white); font-size: 17px; text-decoration: none; white-space: nowrap; }
  .social { position: absolute; top: 22px; width: 28px; height: 28px; background: var(--white); opacity: .9; }
  .account-btn { position: absolute; left: 878px; top: 136px; width: 167px; height: 38px; background: var(--green);
    border-bottom: 4px solid #0b8a3a; color: var(--white); font-size: 15px; display: flex; align-items: center; justify-content: center; gap: 8px; }
  .account-btn .divider { width: 1px; height: 22px; background: var(--white); }

  .hero { position: absolute; left: 0; top: 204px; width: 1081px; height: 478px; background: var(--charcoal); }
  .hero-pill { position: absolute; left: 343px; top: 19px; width: 407px; height: 50px; border-radius: 25px; background: var(--pill);
    color: var(--white); font-size: 16px; display: flex; align-items: center; justify-content: center; }
  .video-panel { position: absolute; left: 290px; top: 84px; width: 498px; height: 310px; background: var(--white); }
  .video-title { position: absolute; left: 0; width: 498px; text-align: center; font-family: "Fira Sans", Arial, sans-serif; font-weight: 700; }
  .video-title.line-one { top: 122px; font-size: 26px; color: var(--ink); }
  .video-title.line-two { top: 156px; font-size: 33px; }
  .c-yellow { color: var(--yellow); } .c-green { color: var(--green); } .c-blue { color: var(--blue); }
  .play-btn { position: absolute; left: 230px; top: 134px; width: 62px; height: 42px; border-radius: 8px; background: rgba(30,30,30,.85); }
  .video-tools { position: absolute; left: 437px; top: 18px; display: flex; flex-direction: column; gap: 6px; }
  .video-tools svg { display: block; }
  .fullscreen { position: absolute; left: 460px; top: 270px; }
  .cta-btn { position: absolute; left: 365px; top: 426px; width: 349px; height: 36px; background: var(--red); border-bottom: 3px solid #8f1620;
    color: var(--white); font-size: 15px; display: flex; align-items: center; justify-content: center; }

  .tagline { position: absolute; left: 0; top: 682px; width: 1081px; height: 200px; background: var(--white);
    font-family: "Fira Sans", Arial, sans-serif; font-size: 50px; }
  .tagline .lead { position: absolute; left: 174px; top: 14px; color: var(--ink); }
  .tagline .values { position: absolute; left: 318px; top: 80px; }

  .site-footer { position: absolute; left: 0; top: 882px; width: 1081px; height: 318px; background: var(--yellow); }
  .footer-nav a { position: absolute; top: 60px; color: var(--ink); font-size: 19px; text-decoration: none; }
  .footer-brand { position: absolute; left: 678px; top: 28px; width: 388px; height: 169px; background: var(--white);
    display: flex; align-items: center; justify-content: center; gap: 22px; }
  .footer-brand .brand-mark { width: 90px; height: 90px; }
  .footer-brand .brand-name { font-size: 40px; line-height: 1.05; }
  .copyright { position: absolute; left: 0; top: 284px; width: 1081px; text-align: center; font-size: 14px; color: var(--ink); }
</style>
</head>
<body>
  <header class="site-header">
    <div class="brand-box">
      <div class="brand-mark"></div>
      <div class="brand-name">Clear Brief Hub</div>
    </div>
    <nav class="main-nav">
      <a href="#" style="left:246px">Home</a>
      <a href="#" style="left:350px">Guide yourself »</a>
      <a href="#" style="left:475px">Draft yourself</a>
      <a href="#" style="left:674px">Search for a lawyer</a>
      <a href="#" style="left:867px">Get your drafts</a>
    </nav>
    <span class="social" style="left:969px"></span>
    <span class="social" style="left:1007px"></span>
    <span class="social" style="left:1045px"></span>
    <div class="account-btn"><span>Sing in</span><span class="divider"></span><span>Register</span></div>
  </header>

  <section class="hero">
    <div class="hero-pill">Free legal support for you and your business</div>
    <div class="video-panel">
      <div class="video-title line-one">Guide yourself, draft yourself</div>
      <div class="video-title line-two"><span class="c-yellow">Help yourself</span><span class="c-green">, it’s free</span></div>
      <div class="play-btn">
        <svg width="62" height="42" viewBox="0 0 62 42"><polygon points="25,12 25,30 40,21" fill="#fff"/></svg>
      </div>
      <div class="video-tools">
        <svg width="42" height="34" viewBox="0 0 42 34"><rect width="42" height="34" fill="var(--icon-dark)"/><path d="M21 25 L12 16 A5 5 0 0 1 21 10 A5 5 0 0 1 30 16 Z" fill="#fff"/></svg>
        <svg width="42" height="34" viewBox="0 0 42 34"><rect width="42" height="34" fill="var(--icon-dark)"/><circle cx="21" cy="17" r="9" fill="none" stroke="#fff" stroke-width="2.5"/><path d="M21 11 V17 H26" stroke="#fff" stroke-width="2.5" fill="none"/></svg>
        <svg width="42" height="34" viewBox="0 0 42 34"><rect width="42" height="34" fill="var(--icon-dark)"/><circle cx="14" cy="17" r="3" fill="#fff"/><circle cx="28" cy="10" r="3" fill="#fff"/><circle cx="28" cy="24" r="3" fill="#fff"/><path d="M14 17 L28 10 M14 17 L28 24" stroke="#fff" stroke-width="2"/></svg>
      </div>
      <svg class="fullscreen" width="20" height="20" viewBox="0 0 20 20"><rect width="20" height="20" rx="2" fill="var(--icon-dark)"/><path d="M5 8 V5 H8 M12 5 H15 V8 M15 12 V15 H12 M8 15 H5 V12" stroke="#fff" stroke-width="1.6" fill="none"/></svg>
    </div>
    <a class="cta-btn" href="#">click here to register and start drafting for free</a>
  </section>

  <section class="tagline">
    <div class="lead">Making legal services</div>
    <div class="values"><span class="c-yellow">fast, </span><span class="c-green">efficient </span><span class="c-blue">&amp; clear.</span></div>
  </section>

  <footer class="site-footer">
    <nav class="footer-nav">
      <a href="#" style="left:57px">About</a>
      <a href="#" style="left:172px">Contact us</a>
      <a href="#" style="left:346px">Community</a>
    </nav>
    <div class="footer-brand">
      <div class="brand-mark"></div>
      <div class="brand-name">Clear Brief<br>Hub</div>
    </div>
    <p class="copyright">Copyright 2013. Clear Brief Hub</p>
  </footer>
</body>
</html>
```